Bref créative
bussines & member card for Jewelry shop
Marten.K Gold & Jewelry
Bright & Fun-filled
Marten.K
Gold & Jewelry
Jln.Mayor Sulaiman Gg.Kedua No.7B
Pasar Tanjung-Rambutan
Medan-Sumatera Utara
Indonesia
marten.kgoldworks@lumarel.example
this is our logo

```html
<!DOCTYPE html>
<html lang="en">
<head>
<meta charset="UTF-8">
<title>Marten.K Gold &amp; Jewelry — Business Card</title>
<link href="https://fonts.googleapis.com/css2?family=Cinzel:wght@400;600&display=swap" rel="stylesheet">
<style>
  :root {
    --page-bg: #e9e7e4;
    --card-white: #ffffff;
    --band-black: #0b0b0b;
    --band-edge: #8a8a8a;
    --ink-dark: #1a1a1a;
    --ink-light: #f2f2f2;
    --ink-muted: #d8d8d8;
  }
  * { box-sizing: border-box; margin: 0; padding: 0; }
  html, body {
    width: 1200px;
    height: 902px;
    overflow: hidden;
    background: var(--page-bg);
    font-family: "Cinzel", "Times New Roman", serif;
  }
  .business-card {
    position: absolute;
    left: 100px;
    top: 165px;
    width: 1000px;
    height: 572px;
    background: var(--card-white);
    box-shadow: 0 10px 30px rgba(0,0,0,0.18);
    overflow: hidden;
  }
  .brand-mark {
    position: absolute;
    left: 0;
    right: 0;
    top: 34px;
    text-align: center;
    color: var(--ink-dark);
  }
  .brand-mark__dot {
    display: block;
    width: 118px;
    height: 118px;
    margin: 0 auto 14px;
    border: 3px solid var(--ink-dark);
    border-radius: 50%;
  }
  .brand-mark__name {
    font-size: 26px;
    font-weight: 400;
    letter-spacing: 3px;
  }
  .contact-band {
    position: absolute;
    left: 0;
    right: 0;
    top: 236px;
    height: 196px;
    background: var(--band-black);
    border-top: 3px solid var(--band-edge);
    border-bottom: 3px solid var(--band-edge);
  }
  .contact-list {
    position: absolute;
    left: 34px;
    top: 40px;
    list-style: none;
    color: var(--ink-light);
    font-size: 12.5px;
    letter-spacing: 0.8px;
    line-height: 1.5;
  }
  .contact-list li {
    display: flex;
    align-items: flex-start;
    gap: 8px;
    margin-bottom: 3px;
  }
  .contact-icon {
    flex: none;
    width: 15px;
    height: 15px;
    margin-top: 2px;
  }
  .signature-block {
    position: absolute;
    right: 40px;
    top: 40px;
    text-align: right;
    color: var(--ink-light);
  }
  .signature-block__name {
    font-size: 22px;
    font-weight: 600;
    letter-spacing: 2px;
  }
  .signature-block__trade {
    font-size: 15px;
    color: var(--ink-muted);
    letter-spacing: 1px;
    margin-top: 2px;
  }
</style>
</head>
<body>
  <div class="business-card">
    <div class="brand-mark">
      <span class="brand-mark__dot"></span>
      <div class="brand-mark__name">MARTEN.K</div>
    </div>

    <div class="contact-band">
      <ul class="contact-list">
        <li>
          <svg class="contact-icon" viewBox="0 0 16 16"><circle cx="8" cy="8" r="8" fill="#f2f2f2"/><path d="M8 3.5a3 3 0 0 0-3 3c0 2.2 3 6 3 6s3-3.8 3-6a3 3 0 0 0-3-3zm0 4.2a1.2 1.2 0 1 1 0-2.4 1.2 1.2 0 0 1 0 2.4z" fill="#0b0b0b"/></svg>
          <span>Jln.Mayor Sulaiman Gg.Kedua No.7B Pasar<br>Tanjung-Rambutan Medan-Sumatera Utara<br>Indonesia</span>
        </li>
        <li>
          <svg class="contact-icon" viewBox="0 0 16 16"><circle cx="8" cy="8" r="8" fill="#f2f2f2"/><path d="M5.2 4h1.6l.7 2-1 .8a5 5 0 0 0 2.3 2.3l.8-1 2 .7v1.6c0 .4-.4.8-.8.8A6.8 6.8 0 0 1 4.4 4.8c0-.4.4-.8.8-.8z" fill="#0b0b0b"/></svg>
          <span>061-4402170</span>
        </li>
        <li>
          <svg class="contact-icon" viewBox="0 0 16 16"><circle cx="8" cy="8" r="8" fill="#f2f2f2"/><path d="M5.2 4h1.6l.7 2-1 .8a5 5 0 0 0 2.3 2.3l.8-1 2 .7v1.6c0 .4-.4.8-.8.8A6.8 6.8 0 0 1 4.4 4.8c0-.4.4-.8.8-.8z" fill="#0b0b0b"/></svg>
          <span>061-77315246</span>
        </li>
        <li>
          <svg class="contact-icon" viewBox="0 0 16 16"><circle cx="8" cy="8" r="8" fill="#f2f2f2"/><path d="M5.2 4h1.6l.7 2-1 .8a5 5 0 0 0 2.3 2.3l.8-1 2 .7v1.6c0 .4-.4.8-.8.8A6.8 6.8 0 0 1 4.4 4.8c0-.4.4-.8.8-.8z" fill="#0b0b0b"/></svg>
          <span>061-77315281</span>
        </li>
        <li>
          <svg class="contact-icon" viewBox="0 0 16 16"><circle cx="8" cy="8" r="8" fill="#f2f2f2"/><rect x="4" y="5" width="8" height="6" fill="none" stroke="#0b0b0b" stroke-width="1.1"/><path d="M4 5l4 3.3L12 5" fill="none" stroke="#0b0b0b" stroke-width="1.1"/></svg>
          <span>marten.kgoldworks@lumarel.example</span>
        </li>
      </ul>

      <div class="signature-block">
        <div class="signature-block__name">MARTEN.K</div>
        <div class="signature-block__trade">Gold &amp; Jewelry</div>
      </div>
    </div>
  </div>
</body>
</html>
```